house selling company website

i need a website that is to get customers to let us sell their house within 30 days with no sales fees based in the uk. iv uploaded a design i like for the website i own i want a copy of this but for the different logo ect need the house buying logo i own to be changed to house selling company
it needs to be able to flash up to sell your house today contact box to collect their details such as property type, address, number of bedrooms, (estate agents valuation) , best price you can accept after they have seen the main section banner with advertising why use us.
the three reasons in the banner to use us needs to be
1: We will sell your house in 30 days and ensure we take a buyers fee for our service from the buyer meaning your buyer is secured unlike with most estate agents
2: We do not charge you any fees at all! our small fee is charged to the buyer
3: A huge network of investors and private buyers connecting many estate agents, auction houses, investors, and private buyers to ensure a fast sale.

```html
<!DOCTYPE html>
<html lang="en">
<head>
<meta charset="utf-8">
<title>Keyline Homes</title>
<link href="https://fonts.googleapis.com/css2?family=Poppins:wght@400;500;600&display=swap" rel="stylesheet">
<style>
:root{
  --blue:#0b86d0;
  --blue-light:#6fb3db;
  --ink:#1b1b1b;
  --text:#222;
  --grey:#eeeeee;
  --grey-2:#f1f1f1;
  --white:#fff;
}
*{box-sizing:border-box;margin:0;padding:0}
html,body{width:1200px;height:3355px;overflow:hidden}
body{font-family:'Poppins',sans-serif;color:var(--text);background:var(--white);position:relative}
.abs{position:absolute}
.brand{display:flex;align-items:center;gap:10px;font-family:'Poppins',sans-serif;font-weight:500;color:var(--blue)}
.brand .mark{width:22px;height:22px;border-radius:50%;background:var(--blue)}
.btn{position:absolute;display:flex;align-items:center;justify-content:center;font-family:'Poppins',sans-serif;font-weight:400;text-decoration:none}
.btn-blue{background:var(--blue);color:var(--white)}
.btn-white{background:var(--white);color:#1f5fa6}

/* header */
.site-header{position:absolute;left:0;top:0;width:1200px;height:158px;background:var(--white)}
.site-header .brand{left:97px;top:72px;font-size:22px}
.pill{height:51px;border-radius:26px;font-size:21px;gap:18px}

/* hero */
.hero{position:absolute;left:0;top:158px;width:1200px;height:813px;background:var(--grey);overflow:hidden}
.hero h1{position:absolute;left:88px;top:110px;font-size:55px;line-height:60px;font-weight:600;color:var(--ink)}
.hero h1 .accent{color:var(--blue)}
.hero-photo{position:absolute;left:598px;top:147px;width:404px;height:404px;border-radius:50%;background:var(--white);padding:9px}
.hero-photo div{width:100%;height:100%;border-radius:50%;background:linear-gradient(160deg,#3f78c4 0%,#5a8fd0 40%,#d7dde4 60%,#28364a 100%)}
.hero p{position:absolute;left:604px;top:578px;width:460px;font-size:21px;line-height:29px;color:var(--white)}

/* search */
.finder{position:absolute;left:0;top:971px;width:1200px;height:697px;background:linear-gradient(180deg,#2a2e33 0%,#3e4347 45%,#4b4e4a 70%,#26301f 100%)}
.finder h2{position:absolute;left:0;width:1200px;top:80px;text-align:center;font-size:44px;font-weight:600;color:var(--white)}
.field{position:absolute;left:419px;width:367px;height:59px;border:2px solid var(--white);color:#e6e6e6;font-size:21px;padding:0 10px;display:flex;align-items:center;justify-content:space-between}

/* about */
.content{position:absolute;left:0;top:1668px;width:1200px;height:1270px;background:var(--grey-2)}
.section-title{position:absolute;font-size:55px;font-weight:600;color:var(--blue)}
.about-copy{position:absolute;left:105px;top:147px;width:410px;font-size:19px;line-height:26.5px;color:var(--text)}
.frame{position:absolute;background:var(--blue);border-radius:20px}
.photo{position:absolute;border-radius:20px}
.reason{position:absolute;left:518px;width:581px;height:141px;border:2px solid var(--blue);display:flex;align-items:center}
.reason .icon{width:86px;height:86px;border-radius:50%;background:#dde8f0;margin-left:14px;flex:none;display:flex;align-items:center;justify-content:center}
.reason p{margin-left:22px;margin-right:14px;font-size:19px;line-height:26.5px;color:var(--text)}

/* footer */
.site-footer{position:absolute;left:0;top:2938px;width:1200px;height:417px;background:var(--white)}
.site-footer .brand{position:absolute;left:125px;top:178px;font-size:18px}
.col{position:absolute;top:100px}
.col h4{font-size:17px;font-weight:400;color:var(--blue);margin-bottom:14px;letter-spacing:.3px}
.col li{list-style:none;font-size:15px;line-height:26px;color:var(--text)}
.col p{font-size:15px;line-height:26px;color:var(--text)}
.signup{position:absolute;left:861px;top:198px;width:256px;height:53px;border:2px solid var(--ink);display:flex;align-items:center;padding:3px}
.signup span{flex:1;font-size:14px;color:#777;padding-left:2px}
.signup b{width:101px;height:43px;background:var(--ink);color:var(--white);font-weight:500;font-size:15px;display:flex;align-items:center;justify-content:center}
.bottom-bar{position:absolute;left:0;top:330px;width:1200px;height:87px;border-top:1px solid #555}
.bottom-bar p{position:absolute;left:84px;top:20px;font-size:15px}
.social{position:absolute;top:22px;width:20px;height:20px;border-radius:50%;background:var(--ink)}
</style>
</head>
<body>

<header class="site-header">
  <div class="brand abs"><span class="mark"></span>Keyline Homes</div>
  <a class="btn btn-blue pill" style="left:720px;top:53px;width:180px">
    <svg width="22" height="20" viewBox="0 0 22 20"><path d="M2 10h11M9 6l4 4-4 4M15 2h5v16h-5" fill="none" stroke="#fff" stroke-width="2.4"/></svg>Login</a>
  <a class="btn btn-blue pill" style="left:925px;top:53px;width:181px">
    <svg width="22" height="22" viewBox="0 0 22 22"><circle cx="11" cy="7" r="5" fill="#fff"/><path d="M1 22c0-7 5-9 10-9s10 2 10 9z" fill="#fff"/></svg>Register</a>
</header>

<section class="hero">
  <svg class="abs" style="left:0;top:0" width="1200" height="813" viewBox="0 0 1200 813">
    <path d="M0 600 C200 520 420 400 620 420 C800 440 980 420 1200 160 L1200 813 L0 813Z" fill="var(--blue-light)"/>
    <path d="M0 640 C200 560 420 450 620 460 C800 470 1000 450 1200 210 L1200 813 L0 813Z" fill="var(--blue)"/>
    <path d="M0 665 C200 590 420 475 620 485 C800 495 1000 475 1200 240 L1200 813 L0 813Z" fill="var(--ink)"/>
  </svg>
  <h1><span class="accent">We Can Find</span><br>Just Right Property<br><span class="accent">For You</span></h1>
  <div class="hero-photo"><div role="img" aria-label="Modern high-rise apartment building against a blue sky"></div></div>
  <p>Lorem ipsum dolor sit amet, consectetur adipiscing elit, sed do eiusmod tempor</p>
  <a class="btn btn-white" style="left:600px;top:680px;width:186px;height:51px;font-size:20px">Read More</a>
</section>

<section class="finder" role="img" aria-label="Dusk view of a house with palm trees and lawn, darkened">
  <h2>The Fastest Way To Swap Your Social Time</h2>
  <div class="field" style="top:200px">Property Type<svg width="12" height="8"><path d="M1 1l5 5 5-5" fill="none" stroke="#fff" stroke-width="2"/></svg></div>
  <div class="field" style="top:277px">Address<svg width="12" height="8"><path d="M1 1l5 5 5-5" fill="none" stroke="#fff" stroke-width="2"/></svg></div>
  <div class="field" style="top:355px">Number Of Bedrooms<svg width="12" height="8"><path d="M1 1l5 5 5-5" fill="none" stroke="#fff" stroke-width="2"/></svg></div>
  <div class="field" style="top:432px">Best Price You Can Accept<svg width="12" height="8"><path d="M1 1l5 5 5-5" fill="none" stroke="#fff" stroke-width="2"/></svg></div>
  <a class="btn btn-blue" style="left:507px;top:521px;width:186px;height:51px;font-size:21px">Book Now</a>
</section>

<section class="content">
  <h2 class="section-title" style="left:102px;top:42px">About Us</h2>
  <p class="about-copy">Lorem ipsum dolor sit amet, consectetur adipiscing elit, sed do eiusmod tempor incididunt ut labore et dolore magna aliqua. Quis ipsum suspendisse ultrices gravida. Risus commodo viverra maecenas accumsan lacus vel facilisis. Lorem ipsum dolor sit amet, consectetur adipiscing elit, sed do eiusmod tempor incididunt ut labore et dolore magna aliqua.</p>
  <a class="btn btn-blue" style="left:106px;top:433px;width:186px;height:51px;font-size:21px">Read More</a>
  <div class="frame" style="left:566px;top:41px;width:522px;height:426px"></div>
  <div class="photo" style="left:548px;top:58px;width:523px;height:426px;background:linear-gradient(180deg,#7cc1e6 0%,#c9a57a 35%,#8fa15c 65%,#4f8a2e 100%)" role="img" aria-label="Timber house with red tiled roof among green trees"></div>

  <div class="frame" style="left:102px;top:597px;width:363px;height:575px"></div>
  <div class="photo" style="left:119px;top:614px;width:346px;height:558px;background:linear-gradient(180deg,#9cc0e0 0%,#d3c49a 40%,#7b2a22 70%,#5c6a35 100%)" role="img" aria-label="Red wooden house under autumn trees and blue sky"></div>
  <h2 class="section-title" style="left:519px;top:595px">Why Choose Us</h2>

  <div class="reason" style="top:698px">
    <div class="icon"><svg width="34" height="28" viewBox="0 0 34 28"><rect x="1" y="6" width="32" height="21" rx="5" fill="var(--blue)"/><path d="M12 6V2h10v4" fill="none" stroke="var(--blue)" stroke-width="3"/><rect x="14" y="13" width="6" height="4" fill="#fff"/></svg></div>
    <p>We will sell your house in 30 days and ensure we take a buyers fee for our service from the buyer meaning your buyer is secured unlike with most estate agents</p>
  </div>
  <div class="reason" style="top:861px">
    <div class="icon"><svg width="38" height="30" viewBox="0 0 38 30"><path d="M19 1L1 12l4 3 14-8 14 8 4-3z" fill="var(--blue)"/><path d="M6 17l13-7 13 7v12H6z" fill="var(--blue)"/></svg></div>
    <p>We do not charge you any fees at all! our small fee is charged to the buyer</p>
  </div>
  <div class="reason" style="top:1024px">
    <div class="icon"><svg width="34" height="32" viewBox="0 0 34 32"><rect x="2" y="24" width="4" height="7" fill="var(--blue)"/><rect x="9" y="20" width="4" height="11" fill="var(--blue)"/><rect x="16" y="16" width="4" height="15" fill="var(--blue)"/><rect x="23" y="11" width="4" height="20" fill="var(--blue)"/><path d="M3 20L24 4M17 3h8v8" fill="none" stroke="var(--blue)" stroke-width="3"/></svg></div>
    <p>A huge network of investors and private buyers connecting many estate agents, auction houses, investors, and private buyers to ensure a fast sale.</p>
  </div>
</section>

<footer class="site-footer">
  <div class="brand"><span class="mark"></span>Keyline Homes</div>
  <div class="col" style="left:346px"><h4>QUICK LINKS</h4><ul><li>Home</li><li>About Us</li><li>Why Choose Us</li><li>Contact Us</li><li>Book Now</li></ul></div>
  <div class="col" style="left:600px"><h4>LEGAL</h4><ul><li>Terms Of Use</li><li>Privacy Policy</li><li>Cookies Policy</li><li>Terms And Condition</li></ul></div>
  <div class="col" style="left:860px;width:290px"><h4 style="margin-left:2px">NEWSLETTER</h4><p>Join our newsletter to stay up date with our latest updates</p></div>
  <div class="signup"><span>Enter Your Email</span><b>Sign up</b></div>
  <div class="bottom-bar">
    <p>All rights reserved @ Copyrights 2023</p>
    <span class="social" style="left:958px"></span>
    <span class="social" style="left:1001px"></span>
    <span class="social" style="left:1044px"></span>
    <span class="social" style="left:1087px"></span>
  </div>
</footer>

</body>
</html>
```